improvement on my landing page

We are a fansite platform similar to velbrook.com, quindleo.com , tarvimu.com and gorbelix.com. We are aiming to disrupt this space by a much cheaper and advanced platform to help influencers monetise across different tools.

current lander is https://plumvarra.com/

Looking for a modern, clean, feminine , pink. Current style and other competitors list given feel old and this needs to highlight its a cutting edge product replacing them. Designs I like are www.brisko.app for example.

I need a few elaborations from current site on price differences of competitors, icons and more details on features and several other new sections added. Need a form to capture email , name and phone as this is a coming soon page. Can change later as a signup

attached document is how thee site looks, so need to keep the identity

Target Market(s)

influence's, adult

Font styles to use
Sans Serif

Colors
eea4c8
fefafc
ecdaeb

Requirements
Nice to have
• infographics

```html
<!DOCTYPE html>
<html lang="en">
<head>
<meta charset="utf-8">
<title>Plumvarra – Keep 90% of your earnings</title>
<link href="https://fonts.googleapis.com/css2?family=Comfortaa:wght@400;600;700&display=swap" rel="stylesheet">
<style>
:root{
  --accent:#e3235f;
  --pink:#eea4c8;
  --pink-soft:#f6cfe0;
  --lavender:#ecdaeb;
  --blush:#fefafc;
  --ink:#2d2d33;
  --text:#555560;
  --muted:#8a8a94;
  --slate:#4a4d5e;
  --grey:#cfcfd4;
  --white:#ffffff;
}
*{margin:0;padding:0;box-sizing:border-box}
html,body{width:1200px;height:4156px;overflow:hidden}
body{position:relative;background:var(--white);font-family:"Comfortaa",sans-serif;color:var(--ink)}
.blob{position:absolute;border-radius:50%;z-index:0}
.blob--pink{background:var(--pink)}
.blob--soft{background:var(--pink-soft)}
.blob--lav{background:var(--lavender)}
.blob--slate{background:var(--slate)}
.blob--grey{background:var(--grey)}
.blob--accent{background:var(--accent);opacity:.8}
.layer{position:absolute;z-index:1}

/* header */
.site-header{position:absolute;left:0;top:0;width:1200px;height:113px;background:var(--white);z-index:2}
.brand{position:absolute;left:158px;top:30px;display:flex;align-items:center;gap:18px}
.brand__dot{width:50px;height:50px;border-radius:50%;background:var(--accent)}
.brand__name{font-size:30px;font-weight:600;letter-spacing:1px;color:var(--ink)}
.nav{position:absolute;top:37px;left:644px;display:flex;align-items:center;height:39px;font-size:15px}
.nav a{color:var(--ink);text-decoration:none}
.nav__link{margin-right:30px}
.btn-outline{display:flex;align-items:center;gap:6px;height:39px;width:114px;justify-content:center;border:2px solid var(--accent);border-radius:20px;color:var(--accent)!important;margin-right:8px}
.btn-solid{display:flex;align-items:center;justify-content:center;height:39px;width:114px;border-radius:20px;background:var(--accent);color:var(--white)!important}

/* hero */
.hero{position:absolute;left:0;top:113px;width:1200px;height:460px;background:linear-gradient(100deg,#3b3a3f 0%,#5c5a5e 40%,#8e8579 62%,#2f3140 100%);z-index:1}
.hero__copy{position:absolute;left:148px;top:104px;color:var(--white)}
.hero__title{font-size:33px;font-weight:400;line-height:45px;letter-spacing:.5px}
.hero__title em{font-style:normal;color:var(--accent)}
.hero__lead{margin-top:26px;width:440px;font-size:15px;line-height:22px}
.hero__lead em{font-style:normal;color:var(--accent)}
.btn-pill{display:inline-flex;align-items:center;justify-content:center;background:var(--accent);color:var(--white);border-radius:20px;font-size:15px;text-decoration:none}
.hero .btn-pill{position:absolute;left:2px;top:354px;width:148px;height:36px}

/* why */
.why{position:absolute;left:150px;top:650px;width:900px;height:374px;background:var(--white);box-shadow:0 4px 18px rgba(0,0,0,.12);z-index:1;display:flex}
.why__photo{width:450px;height:100%;background:linear-gradient(135deg,#d9d9d9,#8c8c8c 55%,#4b4f5c)}
.why__body{padding:30px 26px 0 26px;flex:1}
.section-title{font-size:30px;font-weight:400;color:var(--ink)}
.section-title em{font-style:normal;color:var(--accent)}
.why__body p{font-size:13px;line-height:20px;color:var(--text);margin:28px 0 0 10px;text-align:justify}
.why__body p+p{margin-top:16px}
.why__more{display:block;margin:30px 0 0 10px;font-size:13px;color:var(--accent);text-decoration:none}

.heading{position:absolute;left:0;width:1200px;text-align:center;z-index:1}
.heading span{display:inline-block;padding-bottom:4px;border-bottom:3px solid;border-image:linear-gradient(90deg,var(--accent),#6f2a8c) 1}

/* influencers */
.influencer{position:absolute;width:202px;height:224px;box-shadow:0 4px 12px rgba(0,0,0,.2);z-index:1;overflow:hidden}
.influencer__caption{position:absolute;left:0;bottom:0;width:100%;height:32px;background:rgba(40,40,50,.55);color:var(--white);font-size:15px;text-align:center;line-height:32px}

/* features */
.feature{position:absolute;background:var(--white);box-shadow:0 4px 16px rgba(0,0,0,.13);z-index:1;text-align:center;padding:0 14px}
.feature svg{display:block;margin:0 auto}
.feature h3{font-size:12px;font-weight:400;color:var(--accent);line-height:17px}
.feature p{font-size:11px;line-height:20px;color:var(--ink)}
.feature--lead h3{font-size:16px}
.feature--lead p{font-size:14px;line-height:20px}
.dots{position:absolute;left:0;width:1200px;display:flex;justify-content:center;gap:14px;z-index:1}
.dots i{width:9px;height:9px;border-radius:50%;border:1.5px solid var(--ink)}
.dots i.is-active{background:var(--ink)}

/* testimonials */
.avatar{position:absolute;width:150px;height:150px;border-radius:50%;z-index:2;background:linear-gradient(160deg,#b77c62,#5a3a30)}
.quote{position:absolute;width:262px;height:150px;background:var(--white);border-radius:14px;box-shadow:0 4px 16px rgba(0,0,0,.12);z-index:1;padding:40px 20px 0 18px;font-size:11px;line-height:17px;color:var(--text)}
.quote cite{display:block;text-align:right;font-style:normal;margin-top:10px}

/* competitors */
.fee{position:absolute;background:var(--white);box-shadow:0 4px 16px rgba(0,0,0,.12);z-index:1;text-align:center}
.fee__mark{width:72px;height:72px;border-radius:50%;margin:20px auto 0}
.fee__name{font-size:12px;color:var(--accent);margin-top:24px}
.fee__rate{font-size:38px;color:var(--ink);margin-top:26px}
.fee--lead{border:2px solid var(--accent)}
.fee--lead .fee__name{font-size:15px;margin-top:28px}
.fee--lead .fee__rate{font-size:46px;margin-top:32px}

/* signup */
.signup{position:absolute;left:261px;top:3542px;width:676px;height:523px;background:var(--white);box-shadow:0 4px 20px rgba(0,0,0,.12);z-index:1;text-align:center}
.signup h2{margin-top:34px;font-size:32px;font-weight:400}
.signup h2 em{font-style:normal;color:var(--accent)}
.signup__sub{margin-top:12px;font-size:15px;color:var(--text)}
.field{display:block;margin:0 auto;width:479px;height:36px;border:none;background:#f6f6f7;font-family:inherit;font-size:12px;padding-left:22px;color:var(--muted)}
.field::placeholder{color:var(--muted)}
.signup .btn-pill{width:298px;height:36px;border:none;font-family:inherit;font-size:15px}

.footer-links{position:absolute;top:4136px;left:0;width:1200px;font-size:12px;color:var(--muted);z-index:1}
.footer-links a{position:absolute;color:var(--muted);text-decoration:none}
</style>
</head>
<body>

<!-- decorative circles -->
<div class="blob blob--lav" style="left:-120px;top:470px;width:260px;height:160px"></div>
<div class="blob blob--soft" style="left:320px;top:520px;width:190px;height:150px"></div>
<div class="blob blob--soft" style="left:105px;top:830px;width:180px;height:210px;opacity:.5"></div>
<div class="blob blob--lav" style="left:750px;top:900px;width:210px;height:210px;opacity:.5"></div>
<div class="blob blob--pink" style="left:1041px;top:665px;width:370px;height:370px"></div>
<div class="blob blob--pink" style="left:303px;top:1103px;width:74px;height:74px"></div>
<div class="blob blob--lav" style="left:1003px;top:1088px;width:188px;height:188px"></div>
<div class="blob blob--lav" style="left:560px;top:1185px;width:200px;height:200px;opacity:.7"></div>
<div class="blob blob--slate" style="left:-384px;top:1205px;width:800px;height:750px"></div>
<div class="blob blob--lav" style="left:912px;top:1460px;width:370px;height:370px"></div>
<div class="blob blob--soft" style="left:527px;top:1672px;width:188px;height:188px"></div>
<div class="blob blob--pink" style="left:831px;top:1880px;width:370px;height:370px"></div>
<div class="blob blob--soft" style="left:390px;top:2140px;width:180px;height:140px;opacity:.7"></div>
<div class="blob blob--slate" style="left:56px;top:2253px;width:188px;height:188px"></div>
<div class="blob blob--soft" style="left:613px;top:2420px;width:290px;height:290px;opacity:.6"></div>
<div class="blob blob--grey" style="left:1087px;top:2579px;width:74px;height:74px"></div>
<div class="blob blob--accent" style="left:119px;top:2766px;width:74px;height:74px"></div>
<div class="blob blob--lav" style="left:41px;top:2847px;width:370px;height:370px"></div>
<div class="blob blob--lav" style="left:638px;top:2831px;width:370px;height:370px"></div>
<div class="blob blob--accent" style="left:1028px;top:2947px;width:74px;height:74px"></div>
<div class="blob blob--slate" style="left:-263px;top:3195px;width:620px;height:760px"></div>
<div class="blob blob--pink" style="left:937px;top:3200px;width:530px;height:760px"></div>

<header class="site-header">
  <div class="brand"><span class="brand__dot"></span><span class="brand__name">PLUMVARRA</span></div>
  <nav class="nav">
    <a class="nav__link" href="#">Home</a>
    <a class="nav__link" href="#">About Us</a>
    <a class="btn-outline" href="#">
      <svg width="15" height="15" viewBox="0 0 16 16" fill="none" stroke="currentColor" stroke-width="1.5"><circle cx="8" cy="8" r="6.5"/><path d="M5 8h6M8.5 5.5 11 8l-2.5 2.5"/></svg>Log in</a>
    <a class="btn-solid" href="#">Register</a>
  </nav>
</header>

<section class="hero" role="img" aria-label="Photo of two women working together at a laptop in a bright office">
  <div class="hero__copy">
    <h1 class="hero__title">KEEP <em>90%</em> OF YOUR EARNINGS.<br>NO HIDDEN FEES.</h1>
    <p class="hero__lead">Make more with added revenue streams and features for <em>FREE</em>. Maximise you're your fanbase profits with Plumvarra</p>
    <a class="btn-pill" href="#">Get Started</a>
  </div>
</section>

<section class="why">
  <div class="why__photo" role="img" aria-label="Photo of a woman working on a laptop by a window"></div>
  <div class="why__body">
    <h2 class="section-title">WHY CHOOSE <em>PLUMVARRA</em>?</h2>
    <p>Receive 90% of your earnings, with no hidden fees or extras AND with fastest payouts.</p>
    <p>Monetize with monthly subscriptions through private profile feeds and premium social media accounts.</p>
    <p>Private messaging and tipping, premium videos and much more. Start earning more and keeping your profits.</p>
    <a class="why__more" href="#">Read more</a>
  </div>
</section>

<h2 class="heading section-title" style="top:1130px"><span>OUR <em>INFLUENCERS</em></span></h2>

<div class="influencer" style="left:150px;top:1234px;background:linear-gradient(160deg,#8fb7d6,#c7a27a 60%,#4a3a30)" role="img" aria-label="Photo of influencer Elizabeth Williams"><div class="influencer__caption">Elizabeth Williams</div></div>
<div class="influencer" style="left:382px;top:1234px;background:linear-gradient(160deg,#f1f1f1,#c8c8c8 60%,#6e5142)" role="img" aria-label="Photo of influencer Teresa Courtney"><div class="influencer__caption">Teresa Courtney</div></div>
<div class="influencer" style="left:615px;top:1234px;background:linear-gradient(160deg,#f4f4f4,#d8d8d8 60%,#8a8a84)" role="img" aria-label="Photo of influencer Beatrice White"><div class="influencer__caption">Beatrice White</div></div>
<div class="influencer" style="left:847px;top:1234px;background:linear-gradient(160deg,#c7ccd3,#a2906f 60%,#6c5a3e)" role="img" aria-label="Photo of influencer Robie Quinn"><div class="influencer__caption">Robie Quinn</div></div>
<div class="influencer" style="left:150px;top:1495px;background:linear-gradient(160deg,#e6e6e6,#b0a39a 60%,#5d4a40)" role="img" aria-label="Photo of influencer Bonnie Carter"><div class="influencer__caption">Bonnie Carter</div></div>
<div class="influencer" style="left:382px;top:1495px;background:linear-gradient(160deg,#e3346f,#d3286a 55%,#2f3c6a)" role="img" aria-label="Photo of influencer Katherine Sparks"><div class="influencer__caption">Katherine Sparks</div></div>
<div class="influencer" style="left:615px;top:1495px;background:linear-gradient(160deg,#5a8fc8,#f0b32a 55%,#2d4d7a)" role="img" aria-label="Photo of influencer Emmie Watts"><div class="influencer__caption">Emmie Watts</div></div>
<div class="influencer" style="left:847px;top:1495px;background:linear-gradient(160deg,#c0312e,#962320 60%,#3e3030)" role="img" aria-label="Photo of influencer Bruce Wells"><div class="influencer__caption">Bruce Wells</div></div>

<h2 class="heading section-title" style="top:1861px"><span>OUR <em>FEATURES</em></span></h2>

<div class="feature" style="left:150px;top:1987px;width:156px;height:223px">
  <svg style="margin-top:40px" width="38" height="30" viewBox="0 0 38 30" fill="none" stroke="#333" stroke-width="1.6"><rect x="2" y="4" width="34" height="22" rx="2"/><path d="M2 10h34M2 14h34M8 20h8"/></svg>
  <h3 style="margin-top:26px">Fastest Payouts</h3>
  <p style="margin-top:8px">You own your content. Take it down whenever you want</p>
</div>
<div class="feature" style="left:326px;top:1987px;width:156px;height:223px">
  <svg style="margin-top:34px" width="34" height="38" viewBox="0 0 34 38" fill="none" stroke="#333" stroke-width="1.6"><path d="M6 28V17a11 11 0 0 1 22 0v11l3 3H3z"/><path d="M13 34a4 4 0 0 0 8 0M17 2v4"/></svg>
  <h3 style="margin-top:26px">Instant Notifications</h3>
  <p style="margin-top:8px">Never miss a beat. Get custom &amp; instant email updates</p>
</div>
<div class="feature feature--lead" style="left:503px;top:1968px;width:194px;height:261px">
  <svg style="margin-top:42px" width="50" height="50" viewBox="0 0 50 50" fill="none" stroke="#333" stroke-width="1.8"><rect x="6" y="6" width="38" height="30" rx="8"/><path d="M17 36l-3 9 11-9"/></svg>
  <h3 style="margin-top:22px">Private Snapvora</h3>
  <p style="margin-top:10px">Easily sell private snapvora acces and monitor subscriptions</p>
</div>
<div class="feature" style="left:716px;top:1987px;width:157px;height:223px">
  <svg style="margin-top:28px" width="40" height="38" viewBox="0 0 40 38" fill="none" stroke="#333" stroke-width="1.6"><path d="M2 36h36M6 36V24h5v12M15 36V18h5v12M24 36V22h5v14M33 36V12h5v24"/><path d="M4 16l10-8 8 5 12-10"/></svg>
  <h3 style="margin-top:14px">Inteligent Business Data</h3>
  <p style="margin-top:6px">Easily monitor your business and learn from intuitive data</p>
</div>
<div class="feature" style="left:892px;top:1987px;width:157px;height:223px">
  <svg style="margin-top:34px" width="40" height="40" viewBox="0 0 40 40" fill="none" stroke="#333" stroke-width="1.8"><path d="M20 3a17 17 0 1 1-9 31L3 37l3-8A17 17 0 0 1 20 3z"/><circle cx="13" cy="20" r="1.3" fill="#333"/><circle cx="20" cy="20" r="1.3" fill="#333"/><circle cx="27" cy="20" r="1.3" fill="#333"/></svg>
  <h3 style="margin-top:26px">Private Messaging</h3>
  <p style="margin-top:8px">Engage with your fans on a personal level. Your choice</p>
</div>
<div class="dots" style="top:2274px"><i class="is-active"></i><i></i><i></i></div>

<h2 class="heading section-title" style="top:2424px"><span>OUR <em>TESTIMONIALS</em></span></h2>

<div class="avatar" style="left:206px;top:2525px" role="img" aria-label="Portrait of customer John Smith"></div>
<div class="avatar" style="left:525px;top:2525px;background:linear-gradient(160deg,#8a6a55,#3a2a22)" role="img" aria-label="Portrait of customer Alexandra Milles"></div>
<div class="avatar" style="left:843px;top:2525px;background:linear-gradient(160deg,#e66a8a,#d9b08a 55%,#8bb0c7)" role="img" aria-label="Portrait of customer Jules Steen"></div>
<div class="quote" style="left:150px;top:2645px">"Lorem ipsum dolor sit amet, consectetur adipiscing elit, sed do eiusmod tempor incididunt ut labore et dolore magna aliqua."<cite>John Smith</cite></div>
<div class="quote" style="left:468px;top:2645px">"Lorem ipsum dolor sit amet, consectetur adipiscing elit, sed do eiusmod tempor incididunt ut labore et dolore magna aliqua."<cite>Alexandra Milles</cite></div>
<div class="quote" style="left:787px;top:2645px">"Lorem ipsum dolor sit amet, consectetur adipiscing elit, sed do eiusmod tempor incididunt ut labore et dolore magna aliqua."<cite>Jules Steen</cite></div>
<div class="dots" style="top:2840px"><i class="is-active"></i><i></i><i></i></div>

<h2 class="heading section-title" style="top:2990px"><span>COMPETITORS <em>FEES</em></span></h2>

<div class="fee" style="left:150px;top:3111px;width:160px;height:260px"><div class="fee__mark" style="background:#2d2d33"></div><div class="fee__name">Quindleo</div><div class="fee__rate">20%</div></div>
<div class="fee" style="left:323px;top:3111px;width:159px;height:260px"><div class="fee__mark" style="background:#f26a3d"></div><div class="fee__name">Velbrook</div><div class="fee__rate">15%</div></div>
<div class="fee fee--lead" style="left:494px;top:3090px;width:211px;height:302px"><div class="fee__mark" style="background:var(--accent);margin-top:26px"></div><div class="fee__name">PLUMVARRA</div><div class="fee__rate">10%</div></div>
<div class="fee" style="left:711px;top:3111px;width:165px;height:260px"><div class="fee__mark" style="background:#7a5bc7"></div><div class="fee__name">Gorbelix</div><div class="fee__rate">35%</div></div>
<div class="fee" style="left:879px;top:3111px;width:170px;height:260px"><div class="fee__mark" style="background:#2a9ad6"></div><div class="fee__name">Tarvimu</div><div class="fee__rate">43%</div></div>

<form class="signup">
  <h2>CREATE YOUR <em>FREE</em> ACCOUNT</h2>
  <p class="signup__sub">It only takes a few seconds. No credit card required.</p>
  <input class="field" style="margin-top:37px" type="text" placeholder="Username">
  <input class="field" style="margin-top:31px" type="email" placeholder="Email">
  <input class="field" style="margin-top:31px" type="password" placeholder="Password">
  <input class="field" style="margin-top:31px" type="password" placeholder="Confirm Password">
  <button class="btn-pill" style="margin-top:72px" type="submit">Get Started</button>
</form>

<footer class="footer-links">
  <a href="#" style="left:480px">Privacy</a>
  <a href="#" style="left:600px">Terms &amp; Conditions</a>
</footer>

</body>
</html>
```